" Empresa em abertura de firma (status), voltada para o segmento de Headhunter / Jobhunter, Coaching e demais serviços administrativos/treinamento relacionados. "

```html
<!DOCTYPE html>
<html lang="pt-BR">
<head>
<meta charset="UTF-8">
<title>TalentoPrime – Cartão de Visita</title>
<link rel="stylesheet" href="https://fonts.googleapis.com/css2?family=Open+Sans:wght@300;400;600&display=swap">
<style>
  :root {
    --bg: #ecebe8;
    --card: #ffffff;
    --green: #8cc63f;
    --blue: #1c75bc;
    --magenta: #d6338a;
    --orange: #f7941d;
    --purple: #7b4a9e;
    --text: #5b6670;
    --faint: #eef0f2;
  }
  * { box-sizing: border-box; margin: 0; padding: 0; }
  html, body {
    width: 1200px; height: 1200px; overflow: hidden;
    background: var(--bg);
    font-family: "Open Sans", sans-serif;
  }
  .sheet {
    width: 1200px; height: 1200px;
    display: flex; flex-direction: column;
    align-items: center; justify-content: center; gap: 70px;
  }
  .card {
    position: relative;
    width: 900px; height: 500px;
    background: var(--card);
    overflow: hidden;
    box-shadow: 0 6px 24px rgba(0,0,0,0.12);
  }

  /* Front */
  .front-artwork {
    position: absolute; left: -60px; bottom: -70px;
    width: 380px; height: 300px;
    border-radius: 50% 50% 0 0;
    background: radial-gradient(circle at 40% 55%, var(--green) 0 22%, var(--orange) 23% 34%, var(--blue) 35% 52%, rgba(28,117,188,0.15) 53% 70%, transparent 71%);
  }
  .brand {
    position: absolute; right: 150px; top: 200px;
    display: flex; align-items: center; gap: 18px;
  }
  .brand-dot {
    width: 52px; height: 52px; border-radius: 50%;
    background: var(--magenta);
  }
  .brand-name {
    font-size: 52px; font-weight: 600; color: var(--blue);
    letter-spacing: -0.5px;
  }

  /* Back */
  .back-artwork {
    position: absolute; right: -40px; top: -60px;
    width: 380px; height: 260px;
    border-radius: 0 0 50% 50%;
    background: radial-gradient(circle at 45% 40%, var(--magenta) 0 20%, var(--green) 21% 32%, var(--purple) 33% 44%, var(--blue) 45% 56%, rgba(28,117,188,0.12) 57% 70%, transparent 71%);
  }
  .back-watermark {
    position: absolute; left: -40px; top: 90px;
    width: 420px; height: 420px; border-radius: 50%;
    background: radial-gradient(circle, var(--faint) 0 55%, transparent 70%);
  }
  .holder {
    position: absolute; left: 70px; top: 300px;
  }
  .holder-name {
    font-size: 34px; font-weight: 400; color: var(--green);
    letter-spacing: 1px;
  }
  .holder-role {
    font-size: 20px; font-weight: 300; color: var(--text);
    margin-top: 4px;
  }
  .contacts {
    position: absolute; left: 500px; top: 250px;
    list-style: none;
    display: flex; flex-direction: column; gap: 12px;
  }
  .contact {
    display: flex; align-items: center; gap: 14px;
    font-size: 17px; color: var(--text);
  }
  .contact svg { width: 22px; height: 22px; flex: none; }
  .social-dot {
    width: 22px; height: 22px; border-radius: 50%;
    background: var(--orange); flex: none;
  }
  .bottom-band {
    position: absolute; left: 0; bottom: 0;
    width: 100%; height: 12px;
    background: linear-gradient(90deg, var(--blue), var(--green));
  }
</style>
</head>
<body>
<main class="sheet">
  <section class="card card-front">
    <div class="front-artwork" role="img" aria-label="Ilustração colorida de figuras de pessoas e arcos da marca"></div>
    <div class="brand">
      <span class="brand-dot"></span>
      <span class="brand-name">TalentoPrime</span>
    </div>
  </section>

  <section class="card card-back">
    <div class="back-watermark" role="img" aria-label="Símbolo da marca em marca d'água clara"></div>
    <div class="back-artwork" role="img" aria-label="Ilustração colorida de figuras de pessoas e arcos da marca"></div>
    <div class="holder">
      <p class="holder-name">NOME COMPLETO</p>
      <p class="holder-role">Cargo na Função</p>
    </div>
    <ul class="contacts">
      <li class="contact">
        <svg viewBox="0 0 24 24" aria-hidden="true"><path fill="#1c75bc" d="M6.6 10.8a15 15 0 0 0 6.6 6.6l2.2-2.2c.3-.3.7-.4 1-.2 1.1.4 2.3.6 3.6.6.6 0 1 .4 1 1V20c0 .6-.4 1-1 1A17 17 0 0 1 3 4c0-.6.4-1 1-1h3.5c.6 0 1 .4 1 1 0 1.3.2 2.5.6 3.6.1.3 0 .7-.2 1z"/></svg>
        <span>00 0000-0000 | 00 0000-0000</span>
      </li>
      <li class="contact">
        <svg viewBox="0 0 24 24" aria-hidden="true"><rect x="2" y="5" width="20" height="14" rx="2" fill="#8cc63f"/><path d="M3 6l9 7 9-7" stroke="#fff" stroke-width="1.8" fill="none"/></svg>
        <span>contato@talentoprime.com</span>
      </li>
      <li class="contact">
        <svg viewBox="0 0 24 24" aria-hidden="true"><path fill="#d6338a" d="M12 2a7 7 0 0 0-7 7c0 5 7 13 7 13s7-8 7-13a7 7 0 0 0-7-7zm0 9.5A2.5 2.5 0 1 1 12 6.5a2.5 2.5 0 0 1 0 5z"/></svg>
        <span>Rua nome da rua, 00, bairro</span>
      </li>
      <li class="contact">
        <svg viewBox="0 0 24 24" aria-hidden="true"><path fill="#7b4a9e" d="M12 2a7 7 0 0 0-7 7c0 5 7 13 7 13s7-8 7-13a7 7 0 0 0-7-7zm0 9.5A2.5 2.5 0 1 1 12 6.5a2.5 2.5 0 0 1 0 5z"/></svg>
        <span>Cidade - Estado | CEP</span>
      </li>
      <li class="contact">
        <span class="social-dot"></span>
        <span>@talentoprime</span>
      </li>
    </ul>
    <div class="bottom-band"></div>
  </section>
</main>
</body>
</html>
```